Corvanex - Complete Workplace Desk Provisions

Corporate style business card for directors of Franchisor.
CORVANEX is a B2B Franchise.
Card should contain FRONT:
LOGO
NAME (Tomas Pellegrin)
TITLE (Director of Sales)
ADDRESS
Franchise Headquarters - 14 Wrenfield Parade, Burleigh Heads, Qld, 4220. Australia
Phone: 1800 CORVANEX - 1800 531 947
EMAIL - info@corvanex.com.au
WEB - www.corvanex.com.au

BACK: (Bullet points of services)
- Telecommunications
- Phone Systems & Plans
- Web Services
- IT Services
- Print Hardware & Rentals
- Consumable Supplies
- Maintenance & Support

Target Market(s)

Any Business Office environment

Industry/Entity Type

Business

Contact Information for Business Card

LOGO
NAME (Tomas Pellegrin)
TITLE (Director of Sales)
ADDRESS

- Telecommunications
- Phone Systems & Plans
- Web Services
- IT Services
- Consumable Supplies
- Maintenance & Support

Font styles to use
Sans Serif

Requirements
Must have
• Logo
• Corporate Style
Nice to have
• Keep with Logo base colours
Should not have
• Informal aspects

```html
<!DOCTYPE html>
<html lang="en">
<head>
<meta charset="utf-8">
<title>Corvanex Business Card</title>
<link rel="stylesheet" href="https://fonts.googleapis.com/css2?family=Arimo:wght@400;700&display=swap">
<style>
  :root {
    --stage: #2a2523;
    --paper: #ffffff;
    --ink: #1d1d1d;
    --band: #1c1c1c;
    --orange: #e8541e;
    --grey-text: #f2f2f2;
    --faint: #f3d6cc;
  }
  * { margin: 0; padding: 0; box-sizing: border-box; }
  html, body {
    width: 1200px; height: 783px; overflow: hidden;
    background: var(--stage);
    font-family: "Arimo", Arial, sans-serif;
  }
  .stage { position: relative; width: 1200px; height: 783px; }
  .card {
    position: absolute; width: 540px; height: 310px;
    background: var(--paper);
    box-shadow: 0 10px 30px rgba(0,0,0,.45);
    overflow: hidden;
  }

  /* Back of card: services */
  .card-back { left: 40px; top: 110px; }
  .services { position: absolute; left: 44px; top: 40px; color: var(--ink); }
  .services-title { font-size: 17px; font-weight: 700; margin-bottom: 8px; }
  .services-list { list-style: none; font-size: 15px; line-height: 21px; }
  .services-list li::before {
    content: ""; display: inline-block; width: 6px; height: 6px;
    border-radius: 50%; background: var(--orange);
    margin: 0 8px 2px 0; vertical-align: middle;
  }
  .back-name {
    position: absolute; right: 36px; bottom: 40px;
    font-size: 44px; font-weight: 700; letter-spacing: 3px;
    color: var(--faint);
  }

  /* Front of card: identity and contact */
  .card-front { left: 620px; top: 380px; }
  .brand-area {
    height: 132px; display: flex; align-items: center; justify-content: center;
    gap: 14px;
  }
  .brand-mark { width: 22px; height: 22px; border-radius: 50%; background: var(--orange); }
  .brand-name { font-size: 46px; font-weight: 700; letter-spacing: 4px; color: var(--ink); }
  .info-band {
    position: absolute; left: 0; right: 0; bottom: 0; height: 178px;
    background: var(--band); display: flex; align-items: center;
    padding: 0 24px;
  }
  .person { width: 290px; text-align: right; padding-right: 22px; color: var(--grey-text); }
  .person-name { color: var(--orange); font-size: 19px; margin-bottom: 2px; }
  .person-title { font-size: 16px; margin-bottom: 8px; }
  .person-address { font-size: 14px; line-height: 19px; }
  .divider { width: 1px; height: 120px; background: var(--grey-text); }
  .contact { list-style: none; padding-left: 20px; color: var(--grey-text); font-size: 15px; line-height: 26px; }
  .contact li { display: flex; align-items: center; gap: 9px; }
  .contact-icon { width: 15px; height: 15px; flex: none; }
</style>
</head>
<body>
<main class="stage">
  <section class="card card-back" aria-label="Card back">
    <div class="services">
      <h2 class="services-title">Services</h2>
      <ul class="services-list">
        <li>Telecommunications</li>
        <li>Phone Systems &amp; Plans</li>
        <li>Web Services</li>
        <li>IT Services</li>
        <li>Print Hardware &amp; Rentals</li>
        <li>Consumable Supplies</li>
        <li>Maintenance &amp; Support</li>
      </ul>
    </div>
    <div class="back-name">CORVANEX</div>
  </section>

  <section class="card card-front" aria-label="Card front">
    <div class="brand-area">
      <span class="brand-mark"></span>
      <span class="brand-name">CORVANEX</span>
    </div>
    <div class="info-band">
      <div class="person">
        <p class="person-name">Tomas Pellegrin</p>
        <p class="person-title">Director of Sales</p>
        <p class="person-address">Franchise Headquarters - 14<br>Wrenfield Parade, Burleigh Heads,<br>Qld, 4220. Australia</p>
      </div>
      <div class="divider"></div>
      <ul class="contact">
        <li>
          <svg class="contact-icon" viewBox="0 0 16 16"><rect width="16" height="16" rx="2" fill="var(--orange)"/><path d="M5 3.5l2 2-1 1.3c.6 1.3 1.7 2.4 3 3l1.3-1 2 2-1.2 1.7C7.6 12.2 3.8 8.4 3.5 4.7z" fill="var(--band)"/></svg>
          1800 531 947
        </li>
        <li>
          <svg class="contact-icon" viewBox="0 0 16 16"><rect width="16" height="16" rx="2" fill="var(--orange)"/><rect x="3" y="4.5" width="10" height="7" fill="var(--band)"/><path d="M3 4.5l5 4 5-4" stroke="var(--orange)" fill="none"/></svg>
          info@corvanex.com.au
        </li>
        <li>
          <svg class="contact-icon" viewBox="0 0 16 16"><rect width="16" height="16" rx="2" fill="var(--orange)"/><circle cx="8" cy="8" r="4.5" fill="none" stroke="var(--band)" stroke-width="1.3"/><path d="M3.5 8h9M8 3.5c-2 2.5-2 6.5 0 9M8 3.5c2 2.5 2 6.5 0 9" stroke="var(--band)" fill="none"/></svg>
          www.corvanex.com.au
        </li>
      </ul>
    </div>
  </section>
</main>
</body>
</html>
```